innovative investment real estate sales firm

We are a uniquely collabrative firm that seeks to bring a conultative approach to uncovering hidden opportunities for our clients, our website needs to convey our client focused approach. Our firm specializes in the sale of apartment properties in Southern California. We have a team of researchers, transaction coordinators and marketing personal to support our geographically specialized advisers. We need a website that introduces clients to our unique way of better helping them achieve their investment goals.

Target Market(s)

High net worth individuals and families

Industry/Entity Type

Real Estate Agent

Font styles to use
Other font styles liked:
• please use font provided

Requirements
Must have
• Stories of our recent projects
• Features on our people
• email capture for viewing inventory
• content that showcases our unique consultative approach that uncovers unrealized opportunities

```html
<!DOCTYPE html>
<html lang="en">
<head>
<meta charset="utf-8">
<title>Meridian Crest Advisers</title>
<link href="https://fonts.googleapis.com/css2?family=Lato:wght@400;700;900&family=Montserrat:wght@400;500;600&display=swap" rel="stylesheet">
<style>
:root{
  --teal:#11a2bb;
  --slate:#3e4a54;
  --slate-dark:#343c43;
  --green:#8cc63f;
  --ink:#1d1d1d;
  --text:#333;
  --muted:#666;
  --soft:#efefef;
  --line:#d9d9d9;
  --white:#fff;
}
*{box-sizing:border-box;margin:0;padding:0}
html,body{width:1200px;height:2490px;overflow:hidden}
body{font-family:"Lato",Arial,sans-serif;color:var(--text);background:var(--white);position:relative}
a{color:inherit;text-decoration:none}
svg{display:block}

/* top bar */
.topbar{height:47px;background:var(--slate);display:flex;align-items:center;justify-content:space-between;padding:0 80px;color:var(--white);font-size:14px}
.topbar-contact{display:flex;gap:26px;align-items:center}
.topbar-item{display:flex;align-items:center;gap:10px}
.ring{width:28px;height:28px;border:2px solid var(--white);border-radius:50%;display:flex;align-items:center;justify-content:center}
.social{display:flex;gap:6px}
.social-dot{width:30px;height:30px;border-radius:50%;border:2px solid var(--white)}
.dot-a{background:#3b5998}.dot-b{background:#1da1f2}.dot-c{background:#0077b5}.dot-d{background:#dd4b39}

/* header */
.header{height:106px;display:flex;align-items:center;justify-content:space-between;padding:0 80px}
.brand{display:flex;align-items:center;gap:12px}
.brand-mark{width:34px;height:34px;background:var(--teal)}
.brand-name{font-family:"Montserrat",sans-serif;font-weight:600;font-size:21px;color:var(--slate);letter-spacing:1px}
.nav{display:flex;gap:38px;font-family:"Montserrat",sans-serif;font-weight:500;font-size:14px;color:var(--ink)}
.nav span{display:flex;align-items:center;gap:6px}
.caret{width:0;height:0;border-left:4px solid transparent;border-right:4px solid transparent;border-top:5px solid var(--ink)}

/* hero */
.hero{height:511px;position:relative;background:linear-gradient(180deg,#aab3bb 0%,#8d969e 45%,#4d545a 78%,#2f3338 100%);display:flex;align-items:center;justify-content:center}
.hero-title{color:var(--white);font-family:"Montserrat",sans-serif;font-weight:500;font-size:26px;line-height:38px;text-align:center;text-shadow:0 1px 3px rgba(0,0,0,.45);margin-top:-20px}
.hero-dots{position:absolute;bottom:18px;left:50%;transform:translateX(-50%);display:flex;gap:6px}
.hero-dots i{width:12px;height:12px;border-radius:50%;background:var(--white);display:block}
.hero-dots i.on{background:var(--teal);border:2px solid var(--white)}

/* section titles */
.section-title{display:flex;align-items:center;justify-content:center;gap:16px;font-family:"Montserrat",sans-serif;font-size:28px;font-weight:500;color:var(--slate)}
.section-title::before,.section-title::after{content:"";width:36px;height:2px;background:var(--slate)}
.section-title em{font-style:normal;color:var(--teal)}

/* welcome */
.welcome{height:337px;padding-top:48px;text-align:center}
.welcome-lead{margin-top:28px;font-weight:700;font-size:17px;color:var(--ink)}
.welcome-body{width:1040px;margin:18px auto 0;font-size:15px;line-height:26px;color:var(--text)}
.btn{display:inline-block;background:var(--teal);color:var(--white);font-family:"Montserrat",sans-serif;font-weight:500;font-size:15px;padding:11px 14px;margin-top:26px}

/* featured */
.featured{height:681px;background:var(--soft);padding-top:40px}
.cards{display:flex;gap:28px;justify-content:center;margin-top:30px}
.card{width:328px;height:473px;background:var(--white);border:1px solid var(--line);position:relative}
.card-photo{height:206px}
.photo-1{background:linear-gradient(180deg,#9dc3e4,#e8ecef 55%,#6f7c5e)}
.photo-2{background:linear-gradient(180deg,#a9c9e6,#eeeeea 55%,#6e8a55)}
.photo-3{background:linear-gradient(160deg,#1f5f9a,#9cc3e3 55%,#e8f1f8)}
.tag{position:absolute;top:0;left:0;background:var(--green);color:var(--white);font-family:"Montserrat",sans-serif;font-size:15px;font-weight:500;padding:10px 20px}
.card-bar{height:46px;background:var(--teal);display:flex;align-items:center;justify-content:space-between;padding:0 16px 0 18px;color:var(--white);font-weight:700;font-size:14px}
.card-bar span{display:flex;align-items:center;gap:10px}
.price{background:var(--slate);font-weight:400;padding:5px 12px;font-size:14px}
.card-body{padding:22px 18px 0;height:158px}
.card-body h3{font-size:16px;font-weight:700;color:var(--ink)}
.card-body p{margin-top:14px;font-size:12.5px;line-height:20px;color:var(--text)}
.card-meta{border-top:1px solid var(--line);height:61px;display:flex;align-items:center;gap:30px;padding:0 18px;font-size:13px;color:var(--muted)}
.card-meta span{display:flex;align-items:center;gap:7px}
.card-meta small{font-size:10px}
.slider-dots{display:flex;gap:6px;justify-content:center;margin-top:40px}
.slider-dots i{width:9px;height:9px;border-radius:50%;background:#d2d2d2;display:block}
.slider-dots i.on{background:var(--teal)}

/* team */
.team{height:459px;padding-top:45px}
.members{display:flex;justify-content:center;gap:29px;margin-top:30px}
.member{width:240px}
.member-photo{height:242px;position:relative}
.ph-1{background:linear-gradient(180deg,#d9dde0,#b98a5e)}
.ph-2{background:linear-gradient(180deg,#e6eef3,#5d86b8)}
.ph-3{background:linear-gradient(180deg,#b7babd,#8c9196)}
.ph-4{background:linear-gradient(180deg,#d7e4ef,#f0ebe6)}
.member-overlay{position:absolute;left:0;right:0;bottom:0;height:70px;display:flex;flex-direction:column;align-items:center;justify-content:center;color:var(--white);background:rgba(60,66,72,.45)}
.member-overlay b{font-size:14px;font-weight:700;letter-spacing:.5px}
.member-overlay small{font-size:12px;margin-top:4px}
.member-name{height:45px;border-bottom:3px solid #cfcfcf;display:flex;align-items:center;justify-content:center;font-size:14px;font-weight:700;color:var(--ink);letter-spacing:.5px}
.member-links{height:45px;border-bottom:3px solid var(--green);display:flex;align-items:center;justify-content:center;gap:22px}
.member-links i{width:10px;height:10px;border-radius:50%;background:var(--slate);display:block}
.member-links i.green{background:var(--green)}

/* footer */
.footer{height:299px;background:var(--slate);position:relative;color:var(--white)}
.inquiry{position:absolute;left:91px;top:-11px;width:294px;height:277px;background:var(--teal);padding:22px 22px}
.inquiry h4{font-family:"Montserrat",sans-serif;font-weight:600;font-size:17px}
.field{background:var(--white);height:31px;margin-top:10px;color:#999;font-size:12px;font-style:italic;padding:8px 8px}
.field:first-of-type{margin-top:16px}
.field.tall{height:58px}
.submit{display:inline-block;background:var(--green);font-weight:700;font-size:13px;padding:8px 14px;margin-top:14px}
.fcol{position:absolute;top:55px}
.fcol h5{font-family:"Montserrat",sans-serif;font-weight:600;font-size:16px;display:flex;align-items:center;gap:14px}
.fcol h5::after{content:"";width:50px;height:1px;background:#6d7881}
.links{left:446px}
.links ul{list-style:none;margin-top:18px}
.links li{font-size:14px;margin-bottom:15px}
.links li::before{content:"»";margin-right:14px}
.contact{left:688px}
.contact ul{list-style:none;margin-top:18px}
.contact li{display:flex;gap:12px;font-size:14px;margin-bottom:17px}
.contact li div b{display:block;font-size:13px}
.contact li div small{font-size:13px}
.footer-brand{position:absolute;left:995px;top:90px;width:130px;text-align:center}
.footer-brand .brand-mark{width:30px;height:30px;margin:0 auto 8px;background:#b8c0c6}
.footer-brand .name{font-family:"Montserrat",sans-serif;font-weight:600;font-size:15px;color:#d0d6db;letter-spacing:1px}
.footer-brand .social{justify-content:center;margin-top:16px}
.copyright{height:50px;background:var(--slate-dark);color:#c9c9c9;font-size:14px;display:flex;align-items:center;justify-content:center}
</style>
</head>
<body>

<div class="topbar">
  <div class="topbar-contact">
    <div class="topbar-item"><span class="ring"><svg width="14" height="14" viewBox="0 0 24 24"><path fill="#fff" d="M6.6 10.8a15 15 0 0 0 6.6 6.6l2.2-2.2c.3-.3.7-.4 1-.2 1.1.4 2.3.6 3.6.6.6 0 1 .4 1 1V20c0 .6-.4 1-1 1A17 17 0 0 1 3 4c0-.6.4-1 1-1h3.5c.6 0 1 .4 1 1 0 1.3.2 2.5.6 3.6.1.3 0 .7-.2 1z"/></svg></span>(555)-014-2290</div>
    <div class="topbar-item"><span class="ring"><svg width="14" height="12" viewBox="0 0 24 18"><rect x="1" y="1" width="22" height="16" fill="#fff"/><path d="M1 1l11 9 11-9" stroke="#3e4a54" stroke-width="2" fill="none"/></svg></span>info@meridiancrest.com</div>
  </div>
  <div class="social"><span class="social-dot dot-a"></span><span class="social-dot dot-b"></span><span class="social-dot dot-c"></span><span class="social-dot dot-d"></span></div>
</div>

<header class="header">
  <div class="brand"><span class="brand-mark"></span><span class="brand-name">MERIDIAN CREST</span></div>
  <nav class="nav">
    <span>HOME</span><span>ABOUT US <i class="caret"></i></span><span>SERVICES <i class="caret"></i></span><span>FEATURED PROPERTIES <i class="caret"></i></span><span>CONTACT US</span>
  </nav>
</header>

<section class="hero" role="img" aria-label="Office desk with laptop overlooking a city skyline">
  <h1 class="hero-title">We Are A Uniquely Collaborative Firm That Seeks To Bring A New<br>Approach To Uncovering Hidden Opportunities For Our Clients</h1>
  <div class="hero-dots"><i class="on"></i><i></i><i></i><i></i></div>
</section>

<section class="welcome">
  <h2 class="section-title"><span><em>WELCOME TO</em> MERIDIAN CREST</span></h2>
  <p class="welcome-lead">Lorem ipsum dolor sit amet, consectetuer adipiscing elit, sed diam nonummy nibh euismod tincidun.</p>
  <p class="welcome-body">Ut wisi enim ad minim veniam, quis nostrud exerci tation ullamcorper suscipit lobortis nisl ut aliquip ex ea commodo consequat. Duis autem vel eum iriure dolor in hendrerit in vulputate velit esse molestie consequat, vel illum dolore eu feugiat nulla facilisis. am. Lorem ipsum dolor sit amet, conse ctetur piscing elit. Nulla in sollicitudin velit, bibendum velit.Cras velel facilisis ipsum, etptellnow venenatis risus.</p>
  <a class="btn">READ MORE</a>
</section>

<section class="featured">
  <h2 class="section-title"><span><em>FEATURED</em> PROPERTIES</span></h2>
  <div class="cards">
    <article class="card">
      <div class="card-photo photo-1" role="img" aria-label="Modern white two-storey house"></div>
      <span class="tag">SALE</span>
      <div class="card-bar"><span><svg width="14" height="18" viewBox="0 0 14 18"><path fill="#fff" d="M7 0a7 7 0 0 0-7 7c0 5 7 11 7 11s7-6 7-11a7 7 0 0 0-7-7zm0 10a3 3 0 1 1 0-6 3 3 0 0 1 0 6z"/></svg>123 Dollar Smit Amet</span><span class="price">$ 123000</span></div>
      <div class="card-body"><h3>Duis autem vel eum iriure</h3><p>Lorem ipsum dolor sit amet, consectetuer piscing elit, sed diam nonummy nibh euismod tincidunt ut laoreet dolore magna aliquam erat volutpat. Ut wisi enim ad minim veniam.</p></div>
      <div class="card-meta"><span>⤢ 1200 <small>sq ft</small></span><span>▭ 2 Beds</span><span>💧 2 Baths</span></div>
    </article>
    <article class="card">
      <div class="card-photo photo-2" role="img" aria-label="Contemporary house with balcony and garden"></div>
      <span class="tag">RENT</span>
      <div class="card-bar"><span><svg width="14" height="18" viewBox="0 0 14 18"><path fill="#fff" d="M7 0a7 7 0 0 0-7 7c0 5 7 11 7 11s7-6 7-11a7 7 0 0 0-7-7zm0 10a3 3 0 1 1 0-6 3 3 0 0 1 0 6z"/></svg>123 Dollar Smit Amet</span><span class="price">$ 2120</span></div>
      <div class="card-body"><h3>Duis autem vel eum iriure</h3><p>Lorem ipsum dolor sit amet, consectetuer piscing elit, sed diam nonummy nibh euismod tincidunt ut laoreet dolore magna aliquam erat volutpat. Ut wisi enim ad minim veniam.</p></div>
      <div class="card-meta"><span>⤢ 1200 <small>sq ft</small></span><span>▭ 2 Beds</span><span>💧 2 Baths</span></div>
    </article>
    <article class="card">
      <div class="card-photo photo-3" role="img" aria-label="Glass-walled office interior in blue tones"></div>
      <span class="tag">SALE</span>
      <div class="card-bar"><span><svg width="14" height="18" viewBox="0 0 14 18"><path fill="#fff" d="M7 0a7 7 0 0 0-7 7c0 5 7 11 7 11s7-6 7-11a7 7 0 0 0-7-7zm0 10a3 3 0 1 1 0-6 3 3 0 0 1 0 6z"/></svg>123 Dollar Smit Amet</span><span class="price">$ 560000</span></div>
      <div class="card-body"><h3>Duis autem vel eum iriure</h3><p>Lorem ipsum dolor sit amet, consectetuer piscing elit, sed diam nonummy nibh euismod tincidunt ut laoreet dolore magna aliquam erat volutpat. Ut wisi enim ad minim veniam.</p></div>
      <div class="card-meta"><span>⤢ 1200 <small>sq ft</small></span><span>▭ 2 Beds</span><span>💧 2 Baths</span></div>
    </article>
  </div>
  <div class="slider-dots"><i class="on"></i><i></i><i></i><i></i></div>
</section>

<section class="team">
  <h2 class="section-title"><span><em>OUR</em> TEAM</span></h2>
  <div class="members">
    <div class="member"><div class="member-photo ph-1" role="img" aria-label="Portrait of a team adviser"></div><div class="member-name">LOREM IPSUMLOR</div></div>
    <div class="member"><div class="member-photo ph-2" role="img" aria-label="Portrait of a team adviser"></div><div class="member-name">LOREM IPSUMLOR</div></div>
    <div class="member"><div class="member-photo ph-3" role="img" aria-label="Portrait of a team adviser"><div class="member-overlay"><b>LOREM IPSUMLOR</b><small>minim veniam, quis consectetuer</small></div></div><div class="member-links"><i></i><i class="green"></i><i></i><i></i><i></i><i></i></div></div>
    <div class="member"><div class="member-photo ph-4" role="img" aria-label="Portrait of a team adviser"></div><div class="member-name">LOREM IPSUMLOR</div></div>
  </div>
</section>

<footer class="footer">
  <form class="inquiry">
    <h4>QUICK INQUIRY</h4>
    <div class="field">Your Name</div>
    <div class="field">Your Email</div>
    <div class="field tall">Message</div>
    <span class="submit">SUBMIT</span>
  </form>
  <div class="fcol links">
    <h5>QUICK LINKS</h5>
    <ul><li>Home</li><li>About Us</li><li>Services</li><li>Featured Properties</li><li>Contact Us</li></ul>
  </div>
  <div class="fcol contact">
    <h5>CONTACT DETAILS</h5>
    <ul>
      <li><svg width="12" height="16" viewBox="0 0 14 18"><path fill="#fff" d="M7 0a7 7 0 0 0-7 7c0 5 7 11 7 11s7-6 7-11a7 7 0 0 0-7-7zm0 10a3 3 0 1 1 0-6 3 3 0 0 1 0 6z"/></svg><div><b>MERIDIAN CREST ADVISERS</b><small>Loren ipsum damet California 60563</small></div></li>
      <li><svg width="14" height="14" viewBox="0 0 24 24"><path fill="#fff" d="M6.6 10.8a15 15 0 0 0 6.6 6.6l2.2-2.2c.3-.3.7-.4 1-.2 1.1.4 2.3.6 3.6.6.6 0 1 .4 1 1V20c0 .6-.4 1-1 1A17 17 0 0 1 3 4c0-.6.4-1 1-1h3.5c.6 0 1 .4 1 1 0 1.3.2 2.5.6 3.6.1.3 0 .7-.2 1z"/></svg>(555)-014-2290</li>
      <li><svg width="14" height="14" viewBox="0 0 16 16"><rect x="4" y="1" width="8" height="4" fill="#fff"/><rect x="1" y="6" width="14" height="6" fill="#fff"/><rect x="4" y="11" width="8" height="4" fill="#fff"/></svg>(555)-014-2290</li>
      <li><svg width="14" height="12" viewBox="0 0 24 18"><rect x="1" y="1" width="22" height="16" fill="none" stroke="#fff" stroke-width="2"/><path d="M1 1l11 9 11-9" stroke="#fff" stroke-width="2" fill="none"/></svg>info@meridiancrest.com</li>
    </ul>
  </div>
  <div class="footer-brand">
    <div class="brand-mark"></div>
    <div class="name">MERIDIAN CREST</div>
    <div class="social"><span class="social-dot dot-a"></span><span class="social-dot dot-b"></span><span class="social-dot dot-c"></span><span class="social-dot dot-d"></span></div>
  </div>
</footer>
<div class="copyright">Copyright © 2017 Meridian Crest Advisers. All Rights Reserved.</div>

</body>
</html>
```